TORNWICK Pizza Flyer / Menu

Hello so its a new pizza shop called Tornwick. I need a flyer menu designed . it will be 30cm tall and 10.5cm wide. i made one which i have uploaded but as you can see im not very skillfull design wise. I did want the logo on the front with the photo of the counter in the middle and then half the pizza at the bottom. then on the back i wanted all the different toppings ( doesnt have to be the same pics as i have used ) and then drinks and desserts underneath and our contact details. I dont want to include our signature specials. Also facebook/twitter and instagram logos somewhere. the font i have been using is called 'AR CENA' i have attached a rough sketch i have put together to give you an idea too. thanks

Industry/Entity Type

Shop

```html
<!DOCTYPE html>
<html lang="en">
<head>
<meta charset="utf-8">
<title>Tornwick Pizza Menu</title>
<link href="https://fonts.googleapis.com/css2?family=Cabin:wght@500;700&family=Roboto+Condensed:wght@400;700&display=swap" rel="stylesheet">
<style>
:root{
  --wood-dark:#2a1a10;
  --wood-mid:#4a2e1c;
  --wood-light:#5e3c25;
  --gold:#e2a93f;
  --gold-deep:#c9822a;
  --gold-light:#f1c66a;
  --orange:#e98a24;
  --white:#ffffff;
  --cream:#f6ead2;
  --tag:#d9a646;
}
*{margin:0;padding:0;box-sizing:border-box}
html,body{width:1200px;height:3429px;overflow:hidden}
body{position:relative;background:var(--wood-dark);font-family:"Roboto Condensed",Arial,sans-serif;color:var(--white)}
.wood-backdrop{position:absolute;left:0;top:0;width:1200px;height:3429px;
  background:linear-gradient(90deg,var(--wood-dark) 0%,var(--wood-mid) 25%,var(--wood-light) 50%,var(--wood-mid) 75%,var(--wood-dark) 100%)}
.hero-photo{position:absolute;left:0;top:0;width:1200px;height:730px;
  background:radial-gradient(ellipse at 20% 30%,#d2502c 0%,#b8442a 25%,transparent 55%),
             radial-gradient(ellipse at 80% 35%,#cf6b2e 0%,#b84a26 30%,transparent 60%),
             linear-gradient(180deg,#8a6a52 0%,#6e5442 60%,#5a4433 100%)}
.hero-swoosh{position:absolute;left:0;top:650px;width:1200px;height:180px}
.section-label{position:absolute;height:70px;display:flex;align-items:center;
  background:linear-gradient(180deg,var(--gold-light),var(--orange));
  border:3px solid var(--cream);
  font-family:"Cabin",Arial,sans-serif;font-weight:700;font-size:52px;letter-spacing:2px;color:var(--white)}
.label-build{left:-4px;top:890px;width:400px;padding-left:36px;border-radius:0 12px 12px 0}
.label-drinks-left{left:-4px;top:2180px;width:452px;padding-left:36px;border-radius:0 12px 12px 0}
.label-drinks-right{left:895px;top:2190px;width:310px;padding-left:60px;border-radius:12px 0 0 12px}
.topping{position:absolute;width:180px;margin-left:-90px;text-align:center}
.topping-photo{display:block;width:134px;height:134px;margin:0 auto;border:5px solid var(--orange)}
.topping-name{display:block;margin-top:14px;font-size:25px;line-height:1.05;color:var(--white)}
.divider{position:absolute;left:596px;top:2168px;width:6px;height:560px;
  background:radial-gradient(circle,var(--white) 2.6px,transparent 3px) 0 0/6px 22px repeat-y}
.menu-item{position:absolute;font-family:"Cabin",Arial,sans-serif;font-weight:500;font-size:42px;color:var(--white)}
.drink-name{left:20px}
.dessert-name{right:24px;text-align:right}
.price{position:absolute;width:126px;height:52px;line-height:52px;text-align:center;
  background:linear-gradient(180deg,var(--gold-light),var(--tag));border-radius:5px;
  font-family:"Cabin",Arial,sans-serif;font-weight:700;font-size:36px;color:var(--white)}
.promo{position:absolute;left:0;width:1200px;text-align:center;font-family:"Cabin",Arial,sans-serif}
.promo-title{top:2720px;font-size:72px;font-weight:700;color:var(--gold)}
.promo-sub{top:2800px;font-size:70px;font-weight:700;color:var(--gold)}
.promo-min{top:2885px;font-size:62px;font-weight:500;color:var(--white)}
.promo-phone{top:2965px;font-size:126px;font-weight:700;color:var(--gold);letter-spacing:3px}
.footer-band{position:absolute;left:0;top:3132px;width:1200px;height:297px;
  background:linear-gradient(180deg,var(--gold-light),var(--gold-deep));border-top:6px solid var(--cream)}
.footer-line{position:absolute;left:0;width:1200px;text-align:center;font-family:"Cabin",Arial,sans-serif;font-weight:700;font-size:54px;color:var(--white)}
.footer-line-one{top:3160px}
.footer-line-two{top:3228px}
.social{position:absolute;left:0;top:3310px;width:1200px;display:flex;justify-content:center;align-items:center;gap:22px}
.social-mark{width:86px;height:86px;border-radius:14px;background:var(--white)}
.social-name{font-family:"Cabin",Arial,sans-serif;font-weight:700;font-size:64px;color:var(--white)}
</style>
</head>
<body>
<div class="wood-backdrop" role="img" aria-label="Dark wooden plank background"></div>
<div class="hero-photo" role="img" aria-label="Photo of wood-fired pizzas with slices, tomato and basil on a wooden table"></div>
<svg class="hero-swoosh" viewBox="0 0 1200 180" preserveAspectRatio="none">
  <path d="M0 60 Q600 140 1200 40 L1200 90 Q600 190 0 110 Z" fill="#e2a93f"/>
  <path d="M0 110 Q600 190 1200 90 L1200 110 Q600 200 0 130 Z" fill="#2a1a10" opacity="0.6"/>
</svg>

<div class="section-label label-build">BUILD IT</div>

<div class="topping" style="left:95px;top:1010px"><span class="topping-photo" role="img" aria-label="Pineapple" style="background:#e8c63a"></span><span class="topping-name">Pineapple</span></div>
<div class="topping" style="left:286px;top:1010px"><span class="topping-photo" role="img" aria-label="Pepperoni" style="background:#d8582e"></span><span class="topping-name">Pepperoni</span></div>
<div class="topping" style="left:488px;top:1010px"><span class="topping-photo" role="img" aria-label="Red pepper" style="background:#c42a1e"></span><span class="topping-name">Red<br>Pepper</span></div>
<div class="topping" style="left:697px;top:1010px"><span class="topping-photo" role="img" aria-label="Black olives" style="background:#1c1c20"></span><span class="topping-name">Black<br>Olive</span></div>
<div class="topping" style="left:899px;top:1010px"><span class="topping-photo" role="img" aria-label="Spinach" style="background:#3f8a2e"></span><span class="topping-name">Spinach</span></div>
<div class="topping" style="left:1093px;top:1010px"><span class="topping-photo" role="img" aria-label="Garlic" style="background:#e9e2cf"></span><span class="topping-name">Garlic</span></div>

<div class="topping" style="left:95px;top:1238px"><span class="topping-photo" role="img" aria-label="Green olives" style="background:#a8b62a"></span><span class="topping-name">Green<br>Olive</span></div>
<div class="topping" style="left:286px;top:1238px"><span class="topping-photo" role="img" aria-label="Ricotta" style="background:#ecebe6"></span><span class="topping-name">Ricotta</span></div>
<div class="topping" style="left:488px;top:1238px"><span class="topping-photo" role="img" aria-label="Green pepper" style="background:#3c9a2a"></span><span class="topping-name">Green<br>Pepper</span></div>
<div class="topping" style="left:697px;top:1238px"><span class="topping-photo" role="img" aria-label="Red onion" style="background:#8e3a6a"></span><span class="topping-name">Onion</span></div>
<div class="topping" style="left:899px;top:1238px"><span class="topping-photo" role="img" aria-label="Cheddar cheese" style="background:#eda634"></span><span class="topping-name">Cheddar<br>Cheese</span></div>
<div class="topping" style="left:1093px;top:1238px"><span class="topping-photo" role="img" aria-label="Basil" style="background:#2e7a26"></span><span class="topping-name">Basil</span></div>

<div class="topping" style="left:95px;top:1463px"><span class="topping-photo" role="img" aria-label="Pulled beef" style="background:#7a3e24"></span><span class="topping-name">Pulled<br>Beef</span></div>
<div class="topping" style="left:286px;top:1463px"><span class="topping-photo" role="img" aria-label="Mushrooms" style="background:#b89a7a"></span><span class="topping-name">Mushroom</span></div>
<div class="topping" style="left:488px;top:1463px"><span class="topping-photo" role="img" aria-label="Diced tomato" style="background:#d8461e"></span><span class="topping-name">Tomato</span></div>
<div class="topping" style="left:697px;top:1463px"><span class="topping-photo" role="img" aria-label="Salami" style="background:#b04a4a"></span><span class="topping-name">Salami</span></div>
<div class="topping" style="left:899px;top:1463px"><span class="topping-photo" role="img" aria-label="Capers" style="background:#6f8a34"></span><span class="topping-name">Capers</span></div>
<div class="topping" style="left:1093px;top:1463px"><span class="topping-photo" role="img" aria-label="Anchovies" style="background:#8a6a4a"></span><span class="topping-name">Anchovies</span></div>

<div class="topping" style="left:95px;top:1692px"><span class="topping-photo" role="img" aria-label="Sweetcorn" style="background:#e6b52a"></span><span class="topping-name">Corn</span></div>
<div class="topping" style="left:286px;top:1692px"><span class="topping-photo" role="img" aria-label="Chilli" style="background:#b8281c"></span><span class="topping-name">Chili</span></div>
<div class="topping" style="left:488px;top:1692px"><span class="topping-photo" role="img" aria-label="Barbecue sauce" style="background:#4a1a14"></span><span class="topping-name">B-B-Q</span></div>
<div class="topping" style="left:697px;top:1692px"><span class="topping-photo" role="img" aria-label="Pesto" style="background:#4e9a2a"></span><span class="topping-name">Pesto</span></div>
<div class="topping" style="left:899px;top:1692px"><span class="topping-photo" role="img" aria-label="Chorizo" style="background:#b2361e"></span><span class="topping-name">Chorizo</span></div>
<div class="topping" style="left:1093px;top:1692px"><span class="topping-photo" role="img" aria-label="Parmesan" style="background:#e8cf92"></span><span class="topping-name">Parmesan</span></div>

<div class="topping" style="left:236px;top:1913px"><span class="topping-photo" role="img" aria-label="Mozzarella" style="background:#f1e7c8"></span><span class="topping-name">Mozzarella</span></div>
<div class="topping" style="left:472px;top:1913px"><span class="topping-photo" role="img" aria-label="Pulled chicken" style="background:#c9ad8a"></span><span class="topping-name">Pulled<br>Chicken</span></div>
<div class="topping" style="left:693px;top:1913px"><span class="topping-photo" role="img" aria-label="Jalapeno" style="background:#3c7a22"></span><span class="topping-name">Jalapeno</span></div>
<div class="topping" style="left:933px;top:1913px"><span class="topping-photo" role="img" aria-label="Sweet chilli sauce" style="background:#d8401e"></span><span class="topping-name">Sweet<br>Chili</span></div>

<div class="section-label label-drinks-left">DRINKS</div>
<div class="section-label label-drinks-right">DRINKS</div>
<div class="divider"></div>

<div class="menu-item drink-name" style="top:2290px">Blood Orange</div>
<div class="menu-item drink-name" style="top:2396px">Oraneade</div>
<div class="menu-item drink-name" style="top:2499px">Lemon</div>
<div class="menu-item drink-name" style="top:2602px">Cola Fizz</div>

<div class="price" style="left:420px;top:2291px">0.99</div>
<div class="price" style="left:420px;top:2397px">0.99</div>
<div class="price" style="left:420px;top:2500px">0.99</div>
<div class="price" style="left:420px;top:2603px">0.99</div>

<div class="price" style="left:648px;top:2291px">3.99</div>
<div class="price" style="left:648px;top:2397px">2.49</div>
<div class="price" style="left:648px;top:2500px">2.49</div>
<div class="price" style="left:648px;top:2603px">2.49</div>

<div class="menu-item dessert-name" style="top:2323px">Banana Choco Pizza</div>
<div class="menu-item dessert-name" style="top:2426px">CReme Brulee</div>
<div class="menu-item dessert-name" style="top:2526px">Tiramisu</div>
<div class="menu-item dessert-name" style="top:2628px">Choco Dream Cake</div>

<div class="promo promo-title">Wood Stone Pizza Delivered</div>
<div class="promo promo-sub">hot to your door step</div>
<div class="promo promo-min">minimum order of £12</div>
<div class="promo promo-phone">0208 555 0187</div>

<div class="footer-band"></div>
<div class="footer-line footer-line-one">Follow us for updates, offers and if</div>
<div class="footer-line footer-line-two">your lucky.... A FREE PIZZA</div>
<div class="social">
  <span class="social-mark"></span>
  <span class="social-name">@Tornwick</span>
</div>
</body>
</html>
```